Neues Flyer-Design gesucht
Zielgruppe
siehe Homepage www.lirok-bremen.de
Aufgabenstellung
Wir haben bereits einen Flyer und wünschen uns einen neuen, mit weniger Text und anderen Bildern. Wir sind auch offen für ein anderes Format.
In der Datei flyer_ueberarbeitung.docx haben wir andere Texte, sind jedoch nicht zufrieden damit und wünsche professionelle Hilfe :)

```html
<!DOCTYPE html>
<html lang="de">
<head>
<meta charset="utf-8">
<title>Lirok Soziale Dienste – Flyer Hilfen zur Erziehung</title>
<link rel="stylesheet" href="https://fonts.googleapis.com/css2?family=Open+Sans:ital,wght@0,400;0,600;0,700;1,400;1,600&display=swap">
<style>
  :root{
    --green:#a2bf1c;
    --green-dark:#86a012;
    --green-light:#d9e79a;
    --ink:#3b3b3b;
    --dark:#3a3a3a;
    --paper:#ffffff;
    --bg:#e9e9e9;
    --photo-cool:#a9a6a4;
  }
  *{box-sizing:border-box;margin:0;padding:0}
  html,body{width:840px;height:1200px;overflow:hidden;background:var(--bg)}
  body{font-family:"Open Sans",Arial,sans-serif;color:var(--ink);position:relative}
  .spread{position:absolute;left:20px;width:800px;height:565px;background:var(--paper);overflow:hidden;box-shadow:0 2px 8px rgba(0,0,0,.15)}
  .spread--outside{top:25px}
  .spread--inside{top:610px}
  .spread__art{position:absolute;inset:0}
  .block{position:absolute;font-size:8.6px;line-height:1.38}
  .block p{margin-bottom:7px}
  .heading{color:var(--green);font-weight:700;font-size:13px;margin-bottom:5px}

  /* outside */
  .bubble{left:28px;top:62px;width:222px;color:#fff;font-size:8.4px}
  .bubble .heading{color:#2f3a05;font-size:13px}
  .bubble p{margin-bottom:5px}
  .bubble ul{list-style:none;columns:2;margin:2px 0 4px 6px}
  .bubble li{break-inside:avoid}
  .bubble li::before{content:"• "}
  .focus{left:24px;top:226px;width:236px}
  .contact{left:300px;top:200px;width:220px;font-size:9px}
  .contact__item{display:flex;align-items:flex-start;gap:8px;margin-top:12px}
  .contact__icon{flex:0 0 16px;width:16px;height:16px;border-radius:50%;background:var(--green);display:flex;align-items:center;justify-content:center}
  .badge{position:absolute;left:698px;top:8px;width:76px;height:76px;border-radius:50%;background:var(--dark);color:#fff;font-size:8px;line-height:1.35;display:flex;align-items:center;justify-content:center;text-align:center;border:3px solid #fff;box-shadow:0 0 0 1px #bbb}
  .brand{position:absolute;left:565px;top:100px;display:flex;align-items:center;gap:10px}
  .brand__dot{width:22px;height:22px;border-radius:50%;background:var(--green)}
  .brand__name{font-size:30px;font-weight:600;color:#8a8a8a;line-height:1}
  .brand__sub{font-size:13px;font-weight:600;color:#8a8a8a}
  .cover-title{position:absolute;left:548px;top:168px;width:240px;text-align:center;color:var(--green);font-weight:700;font-size:19px}
  .cover-services{position:absolute;left:533px;top:462px;width:267px;text-align:center;color:#fff;font-weight:700;font-size:12.5px;line-height:1.4}
  .cover-url{position:absolute;left:533px;top:530px;width:267px;text-align:center;color:#fff;font-size:11px}

  /* inside */
  .questions{left:28px;top:188px;width:230px;font-size:10.5px;font-style:italic;font-weight:600;line-height:1.35}
  .questions li{list-style:none;position:relative;padding-left:16px;margin-bottom:14px}
  .arrow{position:absolute;left:0;top:2px}
  .about{left:290px;top:154px;width:230px;font-size:8.2px}
  .offer li{list-style:none;position:relative;margin-bottom:6px}
  .offer strong{font-weight:700}
  .help{left:555px;top:30px;width:232px;font-size:8.2px}
  .quote{font-style:italic;font-weight:600}
  .url-band{position:absolute;left:266px;top:532px;width:267px;text-align:center;color:#fff;font-size:11px}
  .closing{position:absolute;left:606px;top:396px;width:176px;height:176px;border-radius:50%;background:var(--dark);border:4px solid #fff;box-shadow:0 0 0 1px #bbb;color:#fff;text-align:center;font-size:9.5px;line-height:1.45;padding:30px 16px 0}
  .closing strong{display:block;margin-top:10px;font-weight:600;font-size:10px}
</style>
</head>
<body>

<section class="spread spread--outside">
  <svg class="spread__art" width="800" height="565" viewBox="0 0 800 565">
    <defs>
      <linearGradient id="fold" x1="0" x2="1">
        <stop offset="0" stop-color="#ffffff"/><stop offset=".85" stop-color="#ffffff"/><stop offset="1" stop-color="#ececec"/>
      </linearGradient>
      <linearGradient id="warm" x1="0" x2="1"><stop offset="0" stop-color="#b9aaa0"/><stop offset="1" stop-color="#d8b29a"/></linearGradient>
      <linearGradient id="hands" x1="0" y1="0" x2="1" y2="1"><stop offset="0" stop-color="#e7d3c8"/><stop offset=".6" stop-color="#d8a99b"/><stop offset="1" stop-color="#c9a08f"/></linearGradient>
    </defs>
    <rect x="0" y="0" width="267" height="565" fill="url(#fold)"/>
    <rect x="267" y="0" width="266" height="565" fill="url(#fold)"/>
    <rect x="533" y="0" width="267" height="565" fill="#f7f7f7"/>
    <path role="img" aria-label="Foto: Hände, die einander halten" d="M0,0 H600 C520,55 430,125 300,118 C190,112 90,70 0,58 Z" fill="url(#warm)"/>
    <path d="M0,58 C90,70 190,112 300,118 C430,125 520,55 600,0" fill="none" stroke="var(--green-light)" stroke-width="7"/>
    <path d="M0,66 C90,78 190,122 300,128 C430,135 525,60 610,0" fill="none" stroke="var(--green)" stroke-width="2"/>
    <path role="img" aria-label="Foto: Vater mit Kleinkind am Laptop" d="M0,420 C90,415 180,420 267,428 V565 H0 Z" fill="#b8b0a8"/>
    <path role="img" aria-label="Foto: belastete Frau mit Händen vor dem Gesicht" d="M267,428 C360,436 450,440 533,440 V565 H267 Z" fill="var(--photo-cool)"/>
    <path d="M0,420 C180,418 360,440 533,440" fill="none" stroke="#dcdcdc" stroke-width="5"/>
    <path role="img" aria-label="Foto: Erwachsenenhand hält Kinderhand" d="M533,210 C620,198 720,196 800,205 V445 H533 Z" fill="url(#hands)"/>
    <path d="M533,445 C640,430 730,418 800,405 V565 H533 Z" fill="var(--green)"/>
    <path d="M533,445 C640,430 730,418 800,405" fill="none" stroke="var(--green-light)" stroke-width="4"/>
    <path d="M18,53 H252 Q264,53 264,65 V192 Q264,204 252,204 H150 L160,222 L128,204 H30 Q18,204 18,192 V65 Q18,53 30,53 Z" fill="var(--green)"/>
  </svg>

  <div class="block bubble">
    <h2 class="heading">Sprachliche Vielfalt</h2>
    <p>Unsere Mitarbeiter/innen verfügen über unterschiedliche kulturelle und sprachliche Hintergründe.</p>
    <p style="margin-bottom:0">Wir haben daher die Möglichkeit Sie auch auf:</p>
    <ul><li>Arabisch</li><li>Kurdisch</li><li>Türkisch</li><li>Englisch</li><li>Russisch</li></ul>
    <p>zu unterstützen.</p>
  </div>

  <div class="block focus">
    <h2 class="heading">Unser Schwerpunkt</h2>
    <p>Wir haben den Anspruch, Menschen mit sozialen als auch psychischen Belastungen zu unterstützen. Diese Belastungen können dabei ihre Ursache in den aktuellen Lebensumständen, traumatischen Erfahrungen und/oder Verlusterfahrungen haben.</p>
    <p>Wir haben uns auf diese Art der Unterstützung spezialisiert. Wir können mit viel Erfahrungen in Bezug auf seelische Belastungen, psychische Erkrankungen und mehrdimensionalen Problemlagen ein umfangreiches und bedarfsorientiertes Hilfsangebot mit und für die KlientInnen gestalten.</p>
  </div>

  <div class="block contact">
    <h2 class="heading">Kontakt</h2>
    <div class="contact__item">
      <span class="contact__icon"><svg width="8" height="10" viewBox="0 0 8 10"><path d="M4,0 A4,4 0 0 1 8,4 C8,7 4,10 4,10 C4,10 0,7 0,4 A4,4 0 0 1 4,0 Z" fill="#fff"/><circle cx="4" cy="4" r="1.5" fill="var(--green)"/></svg></span>
      <span>Lirok – Soziale Dienste<br>Lindenweg 14<br>28195 Bremen-Mitte</span>
    </div>
    <div class="contact__item">
      <span class="contact__icon"><svg width="10" height="10" viewBox="0 0 10 10"><circle cx="5" cy="5" r="4" fill="none" stroke="#fff" stroke-width="1.2"/><path d="M1,5 H9 M5,1 V9" stroke="#fff" stroke-width="1"/></svg></span>
      <span>www.lirok-bremen.com</span>
    </div>
    <div class="contact__item">
      <span class="contact__icon"><svg width="10" height="8" viewBox="0 0 10 8"><rect x="0.5" y="0.5" width="9" height="7" fill="none" stroke="#fff"/><path d="M0.5,0.5 L5,4.5 L9.5,0.5" fill="none" stroke="#fff"/></svg></span>
      <span>info@lirok-bremen.de</span>
    </div>
    <div class="contact__item">
      <span class="contact__icon"><svg width="9" height="10" viewBox="0 0 9 10"><path d="M1,1 Q0,5 4,9 L6,7.5 L4.5,6 L3.5,6.5 Q2,5 2.5,3.5 L3.5,3 L2.5,0.5 Z" fill="#fff"/></svg></span>
      <span>Tel: 0421/555 184 20</span>
    </div>
  </div>

  <div class="badge">Betreuung<br>Begleitung<br>Unterstützung</div>
  <div class="brand">
    <span class="brand__dot"></span>
    <div><div class="brand__name">Lirok</div><div class="brand__sub">Soziale Dienste</div></div>
  </div>
  <h1 class="cover-title">Hilfen zur Erziehung</h1>
  <div class="cover-services">Sozialpädagogische Familienhilfe<br>Erziehungsbeistand<br>Begleitete Umgänge</div>
  <div class="cover-url">www.lirok-bremen.de</div>
</section>

<section class="spread spread--inside">
  <svg class="spread__art" width="800" height="565" viewBox="0 0 800 565">
    <defs>
      <linearGradient id="fold2" x1="0" x2="1">
        <stop offset="0" stop-color="#ffffff"/><stop offset=".85" stop-color="#ffffff"/><stop offset="1" stop-color="#ececec"/>
      </linearGradient>
      <linearGradient id="mother" x1="0" x2="1"><stop offset="0" stop-color="#b7aaa2"/><stop offset=".5" stop-color="#a98470"/><stop offset="1" stop-color="#e3d6cc"/></linearGradient>
      <linearGradient id="heart" x1="0" y1="0" x2="1" y2="1"><stop offset="0" stop-color="#ecd7cb"/><stop offset=".5" stop-color="#d98f80"/><stop offset="1" stop-color="#e6c6b6"/></linearGradient>
    </defs>
    <rect x="0" y="0" width="267" height="565" fill="url(#fold2)"/>
    <rect x="267" y="0" width="266" height="565" fill="url(#fold2)"/>
    <rect x="533" y="0" width="267" height="565" fill="#f8f8f8"/>
    <path role="img" aria-label="Foto: Mutter küsst Kleinkind auf die Wange" d="M0,0 H560 C490,50 400,120 270,138 C170,152 80,152 0,150 Z" fill="url(#mother)"/>
    <path d="M0,150 C80,152 170,152 270,138 C400,120 490,50 560,0" fill="none" stroke="var(--green-light)" stroke-width="7"/>
    <path d="M0,160 C80,162 175,162 275,148 C405,130 495,58 570,0" fill="none" stroke="var(--green)" stroke-width="2"/>
    <path role="img" aria-label="Foto: Hände halten ein rotes Herz" d="M0,360 C90,352 180,352 267,360 V565 H0 Z" fill="url(#heart)"/>
    <path d="M0,360 C90,352 180,352 267,360" fill="none" stroke="#dcdcdc" stroke-width="5"/>
    <path d="M267,500 C420,505 600,500 800,470 V565 H267 Z" fill="var(--green)"/>
    <path d="M267,500 C420,505 600,500 800,470" fill="none" stroke="var(--green-light)" stroke-width="4"/>
  </svg>

  <ul class="block questions">
    <li><svg class="arrow" width="10" height="9" viewBox="0 0 10 9"><path d="M0,4.5 H8 M5,1 L8.5,4.5 L5,8" fill="none" stroke="var(--green)" stroke-width="2"/></svg>Wünschen Sie eine pädagogische Unterstützung für Ihre Familie?</li>
    <li><svg class="arrow" width="10" height="9" viewBox="0 0 10 9"><path d="M0,4.5 H8 M5,1 L8.5,4.5 L5,8" fill="none" stroke="var(--green)" stroke-width="2"/></svg>Sind Sie oder Ihre Familie durch Konflikte belastet, die Sie am liebsten aus der Welt schaffen würden?</li>
    <li><svg class="arrow" width="10" height="9" viewBox="0 0 10 9"><path d="M0,4.5 H8 M5,1 L8.5,4.5 L5,8" fill="none" stroke="var(--green)" stroke-width="2"/></svg>Wünschen Sie sich eine Unterstützung in der Kooperation mit Schulen und Kitas oder auch in Behördenangelegenheiten?</li>
  </ul>

  <div class="block about">
    <h2 class="heading">Wer wir sind</h2>
    <p>Wir sind ein Team von pädagogischen Fachkräften, welches vorrangig Erziehungsberatung leistet.</p>
    <p>Lirok-Soziale Dienste ist ein Träger der Kinder-und Jugendhilfe und bietet eine pädagogische Unterstützung im Rahmen der Hilfen zur Erziehung (SGB VIII) an.</p>
    <p>Das heißt, wir bieten eine pädagogische Unterstützung im Rahmen einer sogenannten „Hilfe zur Erziehung“ an.</p>
    <h2 class="heading" style="margin-top:10px">Was wir anbieten</h2>
    <ul class="offer">
      <li><strong><span style="color:var(--green)">➔</span> Sozialpädagogische Familienhilfe</strong><br>Im Rahmen einer sozialpädagogischen Familienhilfe erfahren Familien direkt vor Ort eine pädagogische Unterstützung, vor allem in Form einer Erziehungsberatung.</li>
      <li><strong><span style="color:var(--green)">➔</span> Erziehungsbeistandschaft, auch für junge Volljährige</strong><br>Mit einer Erziehungsbeistandschaft wird einem Kind oder Jugendlichen exklusiv eine pädagogische Fachkraft an die Seite gestellt. Ziel ist die Unterstützung des Kindes oder Jugendlichen in einer bestimmten Zeit.</li>
      <li><strong><span style="color:var(--green)">➔</span> Begleitete Umgänge</strong><br>Nach einer Trennung der Eltern und/oder Gewaltvorwürfen kann es sinnvoll sein, dass die Kontakte zwischen einem Elternteil und Kind pädagogisch begleitet werden.</li>
    </ul>
  </div>

  <div class="block help">
    <h2 class="heading">Wie Sie Unterstützung erhalten</h2>
    <p>Sollten Sie eine pädagogische Unterstützung wünschen, ist der Allgemeine Soziale Dienst (ASD) des Jugendamtes Ihre erste Anlaufstelle. Mit Hilfe des Behördenfinders wissen Sie, welcher ASD für Sie zuständig ist:<br><em>www.stadtportal-bremen.de/behoerdenfinder</em></p>
    <p>Im Gespräch mit dem ASD wird geprüft, ob ein pädagogischer Bedarf vorliegt. Falls dies zutrifft, wird mit Ihnen besprochen, welche Unterstützung für Sie am besten geeignet sein könnte.</p>
    <h2 class="heading" style="margin-top:10px">Was uns wichtig ist</h2>
    <p>Wir sehen es als unsere Aufgabe an, mit den KlientInnen partizipativ die eigenen Stärken zu aktivieren und sozialraumorientiert zu arbeiten, indem wir Netzwerke und Sozialräume mit den KlientInnen erschließen, die sie im Alltag unterstützen. Die besondere Bedeutung hinsichtlich Sensibilität, Wertschätzung, Offenheit, Toleranz und Transparenz im Umgang mit anderen Menschen kann nicht hoch genug eingeschätzt werden.</p>
    <p class="quote">Keinen verderben lassen, auch nicht sich selber, jeden mit Glück erfüllen, auch sich. Das ist gut. - Hanna Vogt</p>
  </div>

  <div class="url-band">www.lirok-bremen.de</div>
  <div class="closing">Im Laufe eines Lebens können Situationen und Umstände entstehen, welche allein nur schwierig oder gar nicht bewältigt werden können.<strong>Gerne stehen wir Ihnen dabei zur Seite.</strong></div>
</section>

</body>
</html>
```